New Consumer Electronics online shop needs logo & web design

Background:

I'm a web developer who needs a designer for this task. I can do some simple design + UX and back-end programming, so you need to be a gun designer. If you can also cut-up, it's a bonus, but I need someone who understands and breathes design, not interested in a hack design job.

The Job:

I need

(1) a logo for "qlorb" (qlorb.example and qlorb.example.au) pronounced "kuh-lorb". (the logo is going to be more "fun" looking than the web site)
(2) a simple, clean and elegant web design for an online shop

qlorb is an online shop that sells top-line consumer electronic products at heavily discounted prices: think Pomeral laptops, TalkSlates, ReadSlates, Korvex smartphones, SLR or high-end compact Cameras and lenses.

The feel for this business is contemporary, simple, affordable (but not cheap), and someone who understands the technology, and only sells the best brands and latest items.

The web site and web shop is customised (not pagesmith) but should be not too colourful (think pomeral products, platinum, white, black, grey, or SLR cameras, etc) though sparse use of colour is ok.

Basically the final site should convey the products themselves (and their qualities)

Deliverables:

1) Logo, in AI and PNG
2) Web site, in PSD format ready for cut-up. Provide (a) home page design + (b) product page + (c) general "blank" content page (for putting content/ordering/cart, etc). provide sample layer for nav widget.

Criteria:
* good design
* cut-up to CSS/JS/HTML a bonus to win, but if you can't do cut up, just do more 1-2 more PSD samples of the web site.
* basically, the best/good enough design that needs me to do the least work wins! :)

It's a dead easy job for a good designer!
Updates

Sorry if you missed this, but submissions are looking a lot like modified PageSmith templates.

The target platform is not PageSmith.

If you can distinguish yourself from the crowd it would be to your advantage.

Target Market(s)

People looking for top brand electronic goods in a brand they can trust at a price that is (around) 2nd-3rd cheapest.

Industry/Entity Type

Business

Requirements
Must have
• Should be showcasing products. The site does not have many products initially - maybe up to 50.

Needs to be uncluttered.
Should not have
• no cartoon characters.
not too boring - not corporate.

```html
<!DOCTYPE html>
<html lang="en">
<head>
<meta charset="utf-8">
<title>qlorb – Information</title>
<link href="https://fonts.googleapis.com/css2?family=Oswald:wght@400;500;600&family=Arimo:wght@400;700&display=swap" rel="stylesheet">
<style>
:root{
  --bg:#f2f2f2;
  --panel:#ffffff;
  --line:#d9d9d9;
  --ink:#111111;
  --text:#444444;
  --muted:#666666;
  --head:#5f5f5f;
  --accent:#7ab317;
  --nav-top:#7a7a7a;
  --nav-bot:#555555;
  --nav-dark:#3f3f3f;
}
*{margin:0;padding:0;box-sizing:border-box}
html,body{width:1200px;height:969px;overflow:hidden;background:var(--bg)}
body{font-family:"Arimo",Arial,sans-serif;color:var(--text);position:relative}
.abs{position:absolute}
.cond{font-family:"Oswald","Arial Narrow",sans-serif;text-transform:uppercase}

/* header */
.brand{left:170px;top:22px;display:flex;align-items:center;gap:10px}
.brand-dot{width:40px;height:40px;border-radius:50%;background:var(--head)}
.brand-name{font-size:52px;font-weight:400;color:var(--ink);letter-spacing:-1px;line-height:1}
.search-label{left:500px;top:28px;font-size:18px;font-weight:500;color:var(--head);letter-spacing:.3px}
.search{left:500px;top:63px;width:219px;height:27px;border:1px solid #cfcfcf;border-radius:3px;background:#fff;display:flex}
.search span{flex:1}
.search button{width:31px;border:0;border-left:1px solid #cfcfcf;background:#fff;display:flex;align-items:center;justify-content:center}
.cart-icon{left:848px;top:34px}
.cart-text{left:914px;top:28px;font-size:15px;line-height:17px;color:var(--muted)}
.take-order{left:914px;top:67px;width:117px;height:23px;background:var(--accent);color:#fff;border-radius:3px;font-size:15px;font-weight:500;text-align:center;line-height:22px}

/* nav */
.nav{left:170px;top:126px;width:860px;height:34px;border-radius:3px;background:linear-gradient(var(--nav-top),var(--nav-bot));display:flex;box-shadow:0 8px 10px -6px rgba(0,0,0,.35)}
.nav a{color:#fff;text-decoration:none;font-size:13.5px;font-weight:500;line-height:34px;text-align:center;border-right:1px solid #4a4a4a}
.nav .is-active{background:var(--accent)}
.nav .spacer{flex:1;border-right:0}
.nav .account{background:var(--nav-dark);border-right:1px solid #2f2f2f;border-left:1px solid #2f2f2f}

/* main panel */
.panel{left:170px;top:184px;width:860px;height:583px;background:var(--panel);border:1px solid var(--line);border-radius:4px;overflow:hidden}
.sidebar{left:0;top:0;width:249px;height:100%;border-right:1px solid var(--line)}
.panel-title{font-size:25px;font-weight:500;color:var(--head);height:56px;line-height:56px;border-bottom:1px solid var(--line)}
.sidebar .panel-title{padding-left:13px}
.cat-list{list-style:none}
.cat-list li{height:31.6px;line-height:31px;padding-left:13px;font-size:13px;color:var(--muted);background:linear-gradient(#fff,#f4f4f4)}
.cat-list li::before{content:"»";color:var(--accent);margin-right:8px}
.cat-list b{font-weight:400;color:var(--ink)}
.promo{left:0;top:275px;width:249px;border-top:1px solid var(--line);height:308px;text-align:center}
.promo-line1{margin-top:30px;font-size:20px;color:var(--muted)}
.promo-line1 b{font-weight:400;color:#222}
.promo-line2{font-size:26px;color:var(--head);margin-top:4px;text-transform:none}
.promo-line2 em{font-style:normal;color:var(--accent);font-size:34px}
.promo-image{width:132px;height:90px;margin:10px auto 0;border-radius:40px 10px 10px 40px;background:radial-gradient(circle at 35% 50%,#3a3a3a,#0c0c0c 70%)}
.promo-btn{display:inline-block;margin-top:28px;width:77px;height:28px;line-height:28px;background:#777;color:#fff;font-size:14px}
.content{left:249px;top:0;width:610px;height:100%;box-shadow:inset 14px 0 12px -12px rgba(0,0,0,.12)}
.content .panel-title{padding-left:35px}
.article{padding:17px 35px 0 34px}
.article h2{font-size:13.5px;font-weight:400;color:var(--ink);margin-bottom:15px}
.article p{font-size:11.4px;line-height:13.8px;text-align:justify;color:var(--text);margin-bottom:34px}

/* footer */
.foot-col{top:806px;list-style:none;font-size:11px;line-height:15.8px;color:var(--muted)}
.foot-col li::before{content:"»";margin-right:7px;color:#888}
.news-title{left:843px;top:796px;font-size:22px;font-weight:500;color:var(--head)}
.news-input{left:843px;top:833px;width:187px;height:25px;background:#fff;border:1px solid #cfcfcf}
.news-btn{left:843px;top:868px;width:52px;height:22px;background:var(--accent);color:#fff;font-size:12px;line-height:22px;text-align:center}
.foot-rule{left:170px;top:922px;width:860px;height:1px;background:#d4d4d4}
.copyright{left:172px;top:936px;font-size:11px;color:var(--text)}
.copyright b{font-weight:400;font-size:13px;color:var(--ink)}
.social{top:934px;width:24px;height:24px}
.social-a{left:933px;background:#3b5998}
.social-b{left:969px;background:#2aa3dd}
.social-c{left:1007px;background:#0e76a8}
</style>
</head>
<body>

<header>
  <div class="abs brand"><span class="brand-dot"></span><span class="brand-name">qlorb</span></div>
  <div class="abs cond search-label">Product Search</div>
  <div class="abs search"><span></span>
    <button aria-label="Search"><svg width="18" height="18" viewBox="0 0 18 18"><circle cx="10.5" cy="7" r="5" fill="none" stroke="#111" stroke-width="2"/><line x1="7" y1="10.5" x2="2" y2="16" stroke="#111" stroke-width="2.6"/></svg></button>
  </div>
  <svg class="abs cart-icon" width="50" height="55" viewBox="0 0 50 55" aria-label="Cart">
    <path d="M12 20 L20 4 M38 20 L30 4" stroke="#bbb" stroke-width="3" fill="none"/>
    <circle cx="20" cy="4" r="3" fill="#bbb"/><circle cx="30" cy="4" r="3" fill="#bbb"/>
    <rect x="1" y="19" width="48" height="7" rx="2" fill="#c4c4c4"/>
    <path d="M4 27 H46 L42 54 H8 Z" fill="#cfcfcf"/>
    <g stroke="#f2f2f2" stroke-width="2"><line x1="15" y1="32" x2="15" y2="48"/><line x1="20" y1="32" x2="20" y2="48"/><line x1="25" y1="32" x2="25" y2="48"/><line x1="30" y1="32" x2="30" y2="48"/><line x1="35" y1="32" x2="35" y2="48"/></g>
  </svg>
  <div class="abs cart-text">You have no Items<br>in your cart</div>
  <div class="abs cond take-order">Take Order</div>
</header>

<nav class="abs nav cond">
  <a href="#" style="width:81px">Store</a>
  <a href="#" class="is-active" style="width:110px">Information</a>
  <a href="#" style="width:101px">Resellers</a>
  <a href="#" style="width:127px">Shoppers Guide</a>
  <a href="#" style="width:108px">Contact Us</a>
  <a class="spacer"></a>
  <a href="#" class="account" style="width:62px">Login</a>
  <a href="#" class="account" style="width:65px;border-right:0">Signup</a>
</nav>

<main class="abs panel">
  <aside class="abs sidebar">
    <h2 class="cond panel-title">Catagories</h2>
    <ul class="cat-list">
      <li>Laptops &nbsp; (3<b>0 Items)</b></li>
      <li>TalkSlates (12 <b>Items)</b></li>
      <li>ReadSlates (18 <b>Items)</b></li>
      <li>Smartphones (24 <b>Items)</b></li>
      <li>SLR Cameras (16 <b>Items)</b></li>
      <li>Lenses (8 <b>Items)</b></li>
    </ul>
    <div class="abs promo">
      <p class="promo-line1">Halden <b>SLR</b> Lenses</p>
      <p class="cond promo-line2">Get <em>20%</em> Discount</p>
      <div class="promo-image" role="img" aria-label="Photo of a black SLR camera lens"></div>
      <span class="cond promo-btn">More Info</span>
    </div>
  </aside>
  <section class="abs content">
    <h1 class="cond panel-title">Welcome to our site</h1>
    <div class="article">
      <h2>The standard Lorem Ipsum passage, used since the 1500s</h2>
      <p>"Lorem ipsum dolor sit amet, consectetur adipisicing elit, sed do eiusmod tempor incididunt ut labore et dolore magna aliqua. Ut enim ad minim veniam, quis nostrud exercitation ullamco laboris nisi ut aliquip ex ea commodo consequat. Duis aute irure dolor in reprehenderit in voluptate velit esse cillum dolore eu fugiat nulla pariatur. Excepteur sint occaecat cupidatat non proident, sunt in culpa qui officia deserunt mollit anim id est laborum."</p>
      <h2>Section 1.10.32 of "de Finibus Bonorum et Malorum", written by Maro Veltis in 45 BC</h2>
      <p>"Sed ut perspiciatis unde omnis iste natus error sit voluptatem accusantium doloremque laudantium, totam rem aperiam, eaque ipsa quae ab illo inventore veritatis et quasi architecto beatae vitae dicta sunt explicabo. Nemo enim ipsam voluptatem quia voluptas sit aspernatur aut odit aut fugit, sed quia consequuntur magni dolores eos qui ratione voluptatem sequi nesciunt. Neque porro quisquam est, qui dolorem ipsum quia dolor sit amet, consectetur, adipisci velit, sed quia non numquam eius modi tempora incidunt ut labore et dolore magnam aliquam quaerat voluptatem. Ut enim ad minima veniam, quis nostrum exercitationem ullam corporis suscipit laboriosam, nisi ut aliquid ex ea commodi consequatur? Quis autem vel eum iure reprehenderit qui in ea voluptate velit esse quam nihil molestiae consequatur, vel illum qui dolorem eum fugiat quo voluptas nulla pariatur?"</p>
      <h2>1914 translation by J. Pellow</h2>
      <p>"But I must explain to you how all this mistaken idea of denouncing pleasure and praising pain was born and I will give you a complete account of the system, and expound the actual teachings of the great explorer of the truth, the master-builder of human happiness. No one rejects, dislikes, or avoids pleasure itself, because it is pleasure, but because those who do not know how to pursue pleasure rationally encounter consequences that are extremely painful. Nor again is there anyone who loves or pursues or desires to obtain pain of itself, because it is pain, but because occasionally circumstances occur in which toil and pain can procure him some great pleasure. To take a trivial example, which of us ever undertakes laborious physical exercise, except to obtain some advantage from it? But who has any right to find fault with a man who chooses to enjoy a pleasure that has no annoying consequences, or one who avoids a pain that produces no resultant pleasure?"</p>
    </div>
  </section>
</main>

<footer>
  <ul class="abs foot-col" style="left:173px"><li>Laptops</li><li>TalkSlates</li><li>ReadSlates</li><li>Smartphones</li><li>SLR Cameras</li><li>Lenses</li></ul>
  <ul class="abs foot-col" style="left:344px"><li>Terms of use</li><li>Security</li><li>Privacy</li></ul>
  <ul class="abs foot-col" style="left:490px"><li>Payment</li><li>Shipping</li><li>Cancelation and return</li><li>FAQ</li></ul>
  <ul class="abs foot-col" style="left:669px"><li>Mobile Tablets</li><li>Greenbot Phones</li><li>Dual Sim Phones</li><li>Best Smartphones</li></ul>
  <div class="abs cond news-title">Newsletter</div>
  <div class="abs news-input"></div>
  <div class="abs cond news-btn">Signup</div>
  <div class="abs foot-rule"></div>
  <p class="abs copyright">Copyright © <b>qlorb</b> 2013. All Right Reserved</p>
  <span class="abs social social-a" aria-label="Social link"></span>
  <span class="abs social social-b" aria-label="Social link"></span>
  <span class="abs social social-c" aria-label="Social link"></span>
</footer>

</body>
</html>
```